Business Cards Needed For Veterinary Business

Looking for a business card design for a veterinary blood bank. We would like it to be clean and professional on appearance but still warm and inviting. We would like to utilize our logo and similar coloring. We will use our phone number, email, website, employee name, employee title.

We do not want a bunch of animated animal photos but do not need the style to be as clinical as a laboratory or human medical procedure office.

We are looking for some creative ideas to choose from so that we can generate a standout professional business card for our management team to utilize.

Target Market(s)

professionals

Industry/Entity Type

veterinary

Contact Information for Business Card

employee name, employee title, phone number, website URL, email

Font styles to use
Sans Serif

Colors
0054AA
0677BA
7BADD7
CADEEF
E8F1F8
EB3D1F
EC4F4E
F09395
F8D3D4
FCEDEE

Requirements
Nice to have
• creative design
Should not have
• animated photos

```html
<!DOCTYPE html>
<html lang="en">
<head>
<meta charset="utf-8">
<title>Cedarline Animal Blood Bank – Business Cards</title>
<link rel="stylesheet" href="https://fonts.googleapis.com/css2?family=Montserrat:wght@700;800&family=Open+Sans:wght@400;700&display=swap">
<style>
  :root {
    --brand-red: #EB3D1F;
    --brand-blue: #0054AA;
    --ink: #222222;
    --muted: #6b6b6b;
    --card: #ffffff;
    --backdrop: #3a3a3a;
  }
  * { box-sizing: border-box; margin: 0; padding: 0; }
  html, body {
    width: 1200px; height: 689px; overflow: hidden;
    background: var(--backdrop);
  }
  .canvas { position: relative; width: 1200px; height: 689px; }

  .card {
    position: absolute;
    width: 540px; height: 309px;
    background: var(--card);
    box-shadow: 0 10px 30px rgba(0,0,0,.35);
  }
  .card--front { left: 40px; top: 50px; }
  .card--back  { left: 620px; top: 330px; }

  /* Wordmark */
  .wordmark { display: flex; align-items: center; gap: 16px; }
  .wordmark__dot {
    flex: none; border-radius: 50%; background: var(--brand-red);
  }
  .wordmark__text {
    font-family: "Montserrat", sans-serif; font-weight: 800;
    color: var(--brand-red); line-height: 1.05; text-transform: uppercase;
  }
  .card--front .wordmark {
    position: absolute; left: 70px; top: 0; bottom: 0;
  }
  .card--front .wordmark__dot { width: 70px; height: 70px; }
  .card--front .wordmark__text { font-size: 28px; }

  .card--back .wordmark { position: absolute; left: 34px; top: 34px; gap: 10px; }
  .card--back .wordmark__dot { width: 36px; height: 36px; }
  .card--back .wordmark__text { font-size: 15px; }

  .rule {
    position: absolute; left: 240px; top: 128px;
    width: 270px; height: 2px; background: var(--brand-red);
  }
  .address {
    position: absolute; right: 30px; top: 146px;
    font-family: "Open Sans", sans-serif; font-size: 13px;
    color: var(--ink); text-align: right; line-height: 1.45;
  }
  .person { position: absolute; left: 34px; top: 114px; }
  .person__name {
    font-family: "Open Sans", sans-serif; font-weight: 700;
    font-size: 21px; color: var(--brand-red); text-transform: uppercase;
    letter-spacing: .5px;
  }
  .person__title {
    font-family: "Open Sans", sans-serif; font-size: 14px; color: var(--ink);
  }
  .contact {
    position: absolute; left: 34px; top: 200px; list-style: none;
    font-family: "Open Sans", sans-serif; font-size: 14px; color: var(--ink);
  }
  .contact li { display: flex; align-items: center; gap: 8px; line-height: 26px; }
  .contact svg { width: 16px; height: 16px; flex: none; }
</style>
</head>
<body>
<main class="canvas">

  <section class="card card--front" aria-label="Card front">
    <div class="wordmark">
      <span class="wordmark__dot"></span>
      <span class="wordmark__text">Cedarline Animal<br>Blood Bank</span>
    </div>
  </section>

  <section class="card card--back" aria-label="Card back">
    <div class="wordmark">
      <span class="wordmark__dot"></span>
      <span class="wordmark__text">Cedarline Animal<br>Blood Bank</span>
    </div>

    <div class="rule"></div>

    <address class="address">Your address, City<br>State, Zip 1234</address>

    <div class="person">
      <p class="person__name">Daniel Reyes</p>
      <p class="person__title">Managing Director</p>
    </div>

    <ul class="contact">
      <li>
        <svg viewBox="0 0 16 16" aria-hidden="true">
          <circle cx="8" cy="8" r="8" fill="var(--brand-red)"/>
          <path d="M5 4.5c.6-.4 1.2-.3 1.5.3l.6 1.2c.2.4 0 .8-.3 1l-.5.4c.4.9 1.1 1.6 2 2l.4-.5c.3-.3.7-.4 1-.2l1.2.6c.6.3.7.9.3 1.5-.6.8-1.6 1-2.5.6C6.9 10.6 5.4 9.1 4.6 7.3c-.4-.9-.3-1.9.4-2.8z" fill="#fff"/>
        </svg>
        123 456 789
      </li>
      <li>
        <svg viewBox="0 0 16 16" aria-hidden="true">
          <circle cx="8" cy="8" r="8" fill="var(--brand-blue)"/>
          <rect x="4" y="5" width="8" height="6" rx="1" fill="#fff"/>
          <path d="M4 5.5l4 3 4-3" stroke="var(--brand-blue)" stroke-width="1" fill="none"/>
        </svg>
        info@yourgmail.com
      </li>
      <li>
        <svg viewBox="0 0 16 16" aria-hidden="true">
          <circle cx="8" cy="8" r="8" fill="var(--brand-red)"/>
          <circle cx="8" cy="8" r="4.2" stroke="#fff" stroke-width="1" fill="none"/>
          <path d="M3.8 8h8.4M8 3.8c-1.6 2.4-1.6 6 0 8.4M8 3.8c1.6 2.4 1.6 6 0 8.4" stroke="#fff" stroke-width="1" fill="none"/>
        </svg>
        www.yourwebsite.com
      </li>
    </ul>
  </section>

</main>
</body>
</html>
```